Past the Gravel

I need a book cover designed - 6 inches wide x 9 inches tall. I would like it Past the predominantly black and white, with a big bold title as attached:
Past the
GRAVEL
I have attached a black and white photo that I would like to cover the bottom half (or close to it) of the book, with the words: Life Lessons That Helped Build QTR, Pike B Dam, And Transform Loviter & BLUZ TV
By Gavin Melrose
The designs I've included here I don't particularly like, although I think you can see my general idea. He is a black and white man, so I have a back and white photo.
A big bold headline and not overly sized black and white

```html
<!DOCTYPE html>
<html lang="en">
<head>
<meta charset="utf-8">
<title>Past the Gravel — Book Cover</title>
<link href="https://fonts.googleapis.com/css2?family=Bebas+Neue&family=Montserrat:wght@500;600&family=Open+Sans:wght@500&display=swap" rel="stylesheet">
<style>
  :root {
    --ink: #0b0b0b;
    --paper: #f4f4f4;
    --rule: #8a8a8a;
    --photo-light: #5a5a5a;
    --photo-dark: #090909;
  }
  * { margin: 0; padding: 0; box-sizing: border-box; }
  html, body { width: 801px; height: 1200px; overflow: hidden; background: var(--ink); }
  .cover {
    position: relative;
    width: 801px;
    height: 1200px;
    background: var(--ink);
    color: var(--paper);
    overflow: hidden;
  }
  .kicker-row {
    position: absolute;
    top: 58px;
    left: 91px;
    width: 610px;
    display: flex;
    align-items: center;
    gap: 26px;
  }
  .kicker-rule { flex: 1; height: 2px; background: var(--rule); }
  .kicker {
    font-family: "Montserrat", sans-serif;
    font-weight: 600;
    font-size: 58px;
    letter-spacing: 6px;
    line-height: 1;
    text-transform: uppercase;
  }
  .title {
    position: absolute;
    top: 118px;
    left: 0;
    width: 801px;
    text-align: center;
    font-family: "Bebas Neue", sans-serif;
    font-size: 290px;
    line-height: 1;
    letter-spacing: 4px;
  }
  .subtitle {
    position: absolute;
    top: 396px;
    left: 0;
    width: 801px;
    text-align: center;
    font-family: "Montserrat", sans-serif;
    font-weight: 500;
    font-size: 23px;
    line-height: 32px;
    letter-spacing: 2.4px;
    text-transform: uppercase;
  }
  .divider {
    position: absolute;
    top: 555px;
    left: 94px;
    width: 582px;
    height: 2px;
    background: var(--rule);
  }
  .byline {
    position: absolute;
    top: 576px;
    left: 0;
    width: 801px;
    text-align: center;
    font-family: "Open Sans", sans-serif;
    font-weight: 500;
    font-size: 30px;
  }
  .author-photo {
    position: absolute;
    left: 0;
    top: 640px;
    width: 801px;
    height: 560px;
    background: radial-gradient(ellipse 45% 60% at 48% 45%, var(--photo-light) 0%, #2a2a2a 55%, var(--photo-dark) 100%);
  }
</style>
</head>
<body>
  <main class="cover">
    <div class="kicker-row">
      <span class="kicker-rule"></span>
      <span class="kicker">Past the</span>
      <span class="kicker-rule"></span>
    </div>
    <h1 class="title">GRAVEL</h1>
    <p class="subtitle">Life Lessons That Helped Build<br>QTR, Pike B Dam, and Transform<br>Loviter &amp; BLUZ TV</p>
    <div class="divider"></div>
    <p class="byline">By Gavin Melrose</p>
    <div class="author-photo" role="img" aria-label="Black and white portrait photograph of the author in a dark jacket and white shirt"></div>
  </main>
</body>
</html>
```